Corwick Habitat Web

We just need an update/re-design of our existing web site that would include our new company logo and some new photo's. Our current web site can be viewed at www.corwickhabitat.com.au. We would require something very similar to what we have at the moment in terms of content it should all be the same.
The web site would basically act more as a portfolio than one that would generate more business.
We are after a very modern and simple design and maybe something where we can upload our own project photo's and project descriptions as we complete them.

Industry/Entity Type

It Company

```html
<!DOCTYPE html>
<html lang="en">
<head>
<meta charset="utf-8">
<title>Corwick Habitat</title>
<link rel="stylesheet" href="https://fonts.googleapis.com/css2?family=Source+Sans+3:wght@300;400;600&family=Roboto:wght@500&display=swap">
<style>
  :root {
    --ink: #333333;
    --nav: #555555;
    --nav-active: #1a1a1a;
    --brand: #555555;
    --muted: #8a8a8a;
    --paper: #ffffff;
  }
  * { margin: 0; padding: 0; box-sizing: border-box; }
  html, body { width: 960px; height: 1200px; overflow: hidden; background: var(--paper); }
  body { position: relative; font-family: "Source Sans 3", sans-serif; color: var(--ink); }

  .site-header { position: absolute; top: 0; left: 0; width: 960px; height: 112px; }
  .brand { position: absolute; left: 96px; top: 36px; font-family: "Source Sans 3", sans-serif; font-weight: 300; font-size: 31px; color: var(--brand); letter-spacing: 0.5px; }
  .main-nav { position: absolute; right: 96px; top: 45px; display: flex; gap: 18px; }
  .main-nav a { font-family: "Roboto", sans-serif; font-weight: 500; font-size: 13.5px; color: var(--nav); text-decoration: none; letter-spacing: 0.2px; }
  .main-nav a.is-active { color: var(--nav-active); }

  .hero { position: absolute; top: 112px; left: 0; width: 960px; height: 480px;
    background: linear-gradient(160deg, #d9dbdf 0%, #c9cbce 30%, #8e9094 55%, #5b5c5f 80%, #3e3f41 100%); }

  .intro { position: absolute; top: 640px; left: 96px; width: 700px; font-size: 17px; line-height: 21px; font-weight: 400; color: var(--ink); }

  .services { position: absolute; top: 756px; left: 0; width: 960px; }
  .service { position: absolute; width: 160px; margin-left: -80px; text-align: center; }
  .service-photo { width: 128px; height: 128px; border-radius: 50%; margin: 0 auto; }
  .service-name { margin-top: 19px; font-size: 13.5px; line-height: 18px; font-weight: 600; color: var(--ink); }
  .photo-industrial { background: linear-gradient(180deg, #d6d8da 0%, #6f7174 55%, #3c3d3f 100%); }
  .photo-multistorey { background: linear-gradient(180deg, #7c7e82 0%, #b07a4e 45%, #cfd0d2 100%); }
  .photo-commercial { background: linear-gradient(180deg, #3f86d6 0%, #aac8e6 40%, #5a3e32 75%, #2b2b2b 100%); }
  .photo-residential { background: linear-gradient(180deg, #e2e4e8 0%, #2e3548 40%, #1f2433 100%); }
  .photo-facades { background: linear-gradient(180deg, #2a2c30 0%, #b0703e 35%, #d8d6d0 65%, #a9a38f 100%); }

  .values { position: absolute; top: 1012px; left: 0; width: 960px; }
  .value { position: absolute; width: 250px; font-size: 11.8px; line-height: 15.5px; color: var(--ink); }

  .site-footer { position: absolute; top: 1159px; left: 0; width: 960px; text-align: center; font-size: 10px; color: var(--muted); }
</style>
</head>
<body>
  <header class="site-header">
    <div class="brand">Corwick Habitat</div>
    <nav class="main-nav">
      <a href="#" class="is-active">HOME</a>
      <a href="#">RECENT PROJECTS</a>
      <a href="#">OUR SERVICES</a>
      <a href="#">CONTACT US</a>
    </nav>
  </header>

  <div class="hero" role="img" aria-label="Photograph of a modern grey-clad building with a cantilevered upper storey against a cloudy sky"></div>

  <p class="intro">Corwick Habitat Pty Ltd was established in 2005 and has been operating in the Sydney area, but has completed numerous projects outside of Sydney.</p>

  <section class="services">
    <div class="service" style="left:160px">
      <div class="service-photo photo-industrial" role="img" aria-label="Photograph of an industrial office building with louvred facade"></div>
      <div class="service-name">Industrial<br>Offices</div>
    </div>
    <div class="service" style="left:320px">
      <div class="service-photo photo-multistorey" role="img" aria-label="Photograph of a multi storey office building with timber and grey cladding"></div>
      <div class="service-name">Multi Storey<br>Offices</div>
    </div>
    <div class="service" style="left:480px">
      <div class="service-photo photo-commercial" role="img" aria-label="Photograph of a glazed commercial building under blue sky"></div>
      <div class="service-name">Commercial<br>Projects</div>
    </div>
    <div class="service" style="left:640px">
      <div class="service-photo photo-residential" role="img" aria-label="Photograph of a dark clad residential house"></div>
      <div class="service-name">Residental<br>Houses</div>
    </div>
    <div class="service" style="left:800px">
      <div class="service-photo photo-facades" role="img" aria-label="Photograph of an interior foyer with timber ceiling and glass stair"></div>
      <div class="service-name">External<br>Facades</div>
    </div>
  </section>

  <section class="values">
    <p class="value" style="left:97px">The key group of our operating staff have all been involved in the construction industry for well over 20 years.</p>
    <p class="value" style="left:383px">Our employees are skilled and trained and have the experience to deliver the best possible product, safely and on time.</p>
    <p class="value" style="left:641px">At Corwick Habitat we pride ourselves on working together with our clients in providing the best possible service on schedule and within budget.</p>
  </section>

  <footer class="site-footer">© Copyright Corwick Habitat Pty Ltd 2014</footer>
</body>
</html>
```